Business card for my new company (Accounting firm)

I need a business card for my new business Corvane Advisory and Ledger SA. Our services are accounting, tax, audit and financial management. Our customers are small companies, start-ups and new companies. The final design has to show financial security, trust and growth. Please find our logo attached to the business card. Text for the business card: Corvane Advisory and Ledger SA Tomas da Varela Director and Founder Certified Accountant Tel. 022 418 27 35 tv@corvaneconseil.ch www.corvaneconseil.ch Rue des Vergers-Bleus 14 1201 Geneva
Target Market(s)
Our customers are small companies, start-ups and new companies.
Industry/Entity Type
Finance And Accounting
Contact Information for Business Card
Corvane Conseil et Registre SA
Tomas da Varela
Directeur et Fondateur
Expert-comptable diplômé
Tél. 022 418 27 35
tv@corvaneconseil.ch
www.corvaneconseil.ch
Rue des Vergers-Bleus 14
1201 Genève

```html
<!DOCTYPE html>
<html lang="fr">
<head>
<meta charset="utf-8">
<title>Corvane Conseil et Registre SA – Carte de visite</title>
<link href="https://fonts.googleapis.com/css2?family=Raleway:wght@400;500;600;700&display=swap" rel="stylesheet">
<style>
  :root {
    --backdrop: #5e5e5e;
    --card-light: #f3f3f3;
    --card-blue: #1a6292;
    --brand-blue: #1d5f8f;
    --sky-blue: #2fa9dc;
    --text-grey: #4a4a4a;
    --name-dark: #3a3a3a;
    --white: #ffffff;
  }
  * { margin: 0; padding: 0; box-sizing: border-box; }
  html, body {
    width: 1200px; height: 960px; overflow: hidden;
    background: var(--backdrop);
    font-family: "Raleway", sans-serif;
  }
  .canvas { position: relative; width: 1200px; height: 960px; }

  .card {
    position: absolute; left: 270px; width: 660px; height: 377px;
    border-radius: 18px; overflow: hidden;
  }
  .card--front { top: 73px; background: var(--card-light); }
  .card--back { top: 510px; background: var(--card-blue); }

  .edge-tab { position: absolute; right: 0; top: 0; width: 42px; height: 160px; }

  .wordmark {
    position: absolute; display: flex; align-items: center; gap: 12px;
    font-weight: 700; letter-spacing: 3px; text-transform: uppercase;
  }
  .wordmark__square { width: 22px; height: 22px; background: var(--sky-blue); }
  .card--front .wordmark { left: 46px; top: 150px; font-size: 40px; color: var(--name-dark); }
  .card--back .wordmark {
    left: 0; right: 0; top: 160px; justify-content: center;
    font-size: 52px; color: var(--white);
  }
  .card--back .wordmark__square { width: 28px; height: 28px; background: var(--white); }

  .website {
    position: absolute; left: 60px; top: 304px;
    font-size: 15px; color: var(--text-grey);
  }

  .details {
    position: absolute; right: 56px; text-align: right;
    font-size: 15px; line-height: 19px; color: var(--text-grey);
  }
  .person { top: 65px; }
  .person__name { font-size: 20px; font-weight: 700; color: var(--brand-blue); line-height: 26px; }
  .address { top: 211px; }
  .address__company { color: var(--brand-blue); }
  .contact { top: 285px; right: 58px; }
  .contact__line { display: flex; justify-content: flex-end; align-items: center; gap: 9px; }
  .contact__icon { width: 13px; height: 13px; }
</style>
</head>
<body>
<main class="canvas">

  <section class="card card--front" aria-label="Recto de la carte">
    <svg class="edge-tab" viewBox="0 0 42 160" aria-hidden="true">
      <rect x="27" y="0" width="15" height="70" fill="var(--sky-blue)"/>
      <rect x="27" y="70" width="15" height="90" fill="var(--brand-blue)"/>
      <polygon points="0,88 42,58 42,118" fill="var(--brand-blue)"/>
    </svg>

    <div class="wordmark"><span class="wordmark__square"></span>Corvane</div>

    <p class="website">www.corvaneconseil.ch</p>

    <div class="details person">
      <p class="person__name">Tomas da Varela</p>
      <p>Directeur et Fondateur</p>
      <p>Expert - Comptable Diplômé</p>
    </div>

    <div class="details address">
      <p class="address__company">Corvane Conseil et Registre SA</p>
      <p>Rue des Vergers-Bleus 14</p>
      <p>1201 Genève</p>
    </div>

    <div class="details contact">
      <p class="contact__line">022 418 27 35
        <svg class="contact__icon" viewBox="0 0 16 16" aria-hidden="true">
          <path d="M3.5 1.5l2.5 0.5 1 3-1.6 1.2a8 8 0 0 0 4.4 4.4L11 9l3 1 .5 2.5-1.8 1.8C7 14 2 9 1.7 3.3z" fill="var(--brand-blue)"/>
        </svg>
      </p>
      <p class="contact__line">tv@corvaneconseil.ch
        <svg class="contact__icon" viewBox="0 0 16 16" aria-hidden="true">
          <rect x="1.5" y="3.5" width="13" height="9" fill="none" stroke="var(--brand-blue)" stroke-width="1.5"/>
          <path d="M1.5 3.5L8 9l6.5-5.5" fill="none" stroke="var(--brand-blue)" stroke-width="1.5"/>
        </svg>
      </p>
    </div>
  </section>

  <section class="card card--back" aria-label="Verso de la carte">
    <div class="wordmark"><span class="wordmark__square"></span>Corvane</div>
  </section>

</main>
</body>
</html>
```